Law Firm Marketing Post Card to Real Estate Agents

We need a postcard that will be used to market to real estate agents. Something clean, professional and appealing. We're marketing for a specific field (taxes) and are planning on passing out the cards to individual agents and we do not plan on mailing them. We'd like something on the front cover that truly catches someones attention and makes them want to read the back side. Text will read:

Front and Back; front will have very little text. Only the following:
Tax & Legal Strategies for Real Estate Agents
Presented by Birchwell Legal Partners, LLC
5 Tax Strategies Every Real Estate Agent Should Know

BACK COVER:
Most real estate agents are considered 1099 independent contractors, and have never been told that there are money saving strategies that could make a huge difference for them come tax time with just a few easy steps.

With our free consultation, Birchwell has one mission – to teach real estate agents 5 legal and tax planning strategies that could literally save them thousands of dollars.

Please contact us to schedule a one-on-one consultation, or an office presentation, and learn about some of the tax and legal strategies that have helped countless real estate agents and independent contractors:

- Minimize self employment tax
- Deduct 100% of out of pocket medical expenses
- Create wealth
- Deduct 100% of health insurance premiums
- Invest in real estate
- Deduct a portion of a child’s tuition and expenses
- Reduce overall tax liability

For more information, please email our office at: Info@BirchwellLegal.Example.

Target Market(s)

Real Estate Agents

Industry/Entity Type

Real Estate

Requirements
Must have
• Text listed on the front of the card as shown on the attachment.
• Clean, appealing, professional cover.
• must be similar to colors used on our website so that the reader feels like it is from the same company; please include website address on card as well - www.birchwelllegal.example

```html
<!DOCTYPE html>
<html lang="en">
<head>
<meta charset="utf-8">
<title>5 Tax Strategies Every Real Estate Agent Should Know</title>
<link rel="stylesheet" href="https://fonts.googleapis.com/css2?family=Montserrat:wght@300;400;600;800&display=swap">
<style>
  :root {
    --night-deep: #060a13;
    --night-navy: #112039;
    --night-blue: #1b3257;
    --stone-warm: rgba(168, 146, 116, 0.62);
    --stone-shadow: rgba(86, 72, 56, 0.7);
    --city-glow: rgba(120, 118, 140, 0.5);
    --city-warm: rgba(150, 110, 70, 0.35);
    --ink-white: #ffffff;
    --ink-soft: #d4d9e1;
    --brand-blue: #2f6bb3;
  }
  * { margin: 0; padding: 0; box-sizing: border-box; }
  html, body {
    width: 1200px; height: 924px; overflow: hidden;
    background: var(--night-deep);
  }
  .card {
    position: relative; width: 1200px; height: 924px; overflow: hidden;
    font-family: "Montserrat", Arial, sans-serif; color: var(--ink-white);
  }
  .scene {
    position: absolute; inset: 0;
    background:
      radial-gradient(ellipse 150px 280px at 1010px 300px, rgba(6,10,19,0.85), transparent 75%),
      radial-gradient(ellipse 260px 200px at 1030px 640px, var(--stone-warm), transparent 72%),
      radial-gradient(ellipse 360px 300px at 1020px 760px, var(--stone-shadow), transparent 75%),
      radial-gradient(ellipse 330px 90px at 360px 640px, var(--city-glow), transparent 75%),
      radial-gradient(ellipse 260px 70px at 300px 700px, var(--city-warm), transparent 75%),
      radial-gradient(ellipse 480px 130px at 300px 720px, rgba(40,46,66,0.8), transparent 80%),
      linear-gradient(180deg, var(--night-deep) 0%, var(--night-navy) 26%, var(--night-blue) 50%, #172a48 60%, #0b1221 80%, var(--night-deep) 100%);
  }
  .frame-corner {
    position: absolute; width: 70px; height: 70px;
    border-color: var(--ink-white); border-style: solid; border-width: 0;
  }
  .frame-corner.top-left { left: 88px; top: 70px; border-top-width: 3px; border-left-width: 3px; }
  .frame-corner.top-right { left: 691px; top: 70px; border-top-width: 3px; border-right-width: 3px; }
  .frame-corner.bottom-left { left: 88px; top: 328px; border-bottom-width: 3px; border-left-width: 3px; }
  .frame-corner.bottom-right { left: 691px; top: 328px; border-bottom-width: 3px; border-right-width: 3px; }
  .headline { position: absolute; left: 145px; top: 118px; font-weight: 400; }
  .headline-lead { display: flex; align-items: flex-end; line-height: 1; }
  .headline-number { font-weight: 800; font-size: 134px; letter-spacing: -4px; line-height: 0.78; }
  .headline-main { font-weight: 800; font-size: 60px; margin-left: 12px; margin-bottom: -4px; }
  .headline-sub { display: block; font-weight: 600; font-size: 47px; line-height: 64px; margin-top: 6px; }
  .brand-mark {
    position: absolute; left: 92px; top: 826px;
    display: flex; align-items: center; gap: 10px;
    font-weight: 600; font-size: 22px; color: var(--ink-white);
  }
  .brand-mark .brand-square { width: 22px; height: 22px; background: var(--brand-blue); }
  .presenter-line {
    position: absolute; right: 81px; top: 838px;
    font-size: 17px; font-weight: 600; white-space: nowrap; color: var(--ink-white);
  }
  .presenter-line .presented-by { font-weight: 300; color: var(--ink-soft); }
  .website {
    position: absolute; right: 81px; top: 866px;
    font-size: 14px; font-weight: 400; letter-spacing: 0.5px; color: var(--ink-soft);
  }
</style>
</head>
<body>
<main class="card">
  <div class="scene" role="img" aria-label="Night photograph of a lit city skyline with a bronze horse-and-rider statue on a stone pedestal silhouetted against a deep blue sky"></div>

  <span class="frame-corner top-left"></span>
  <span class="frame-corner top-right"></span>
  <span class="frame-corner bottom-left"></span>
  <span class="frame-corner bottom-right"></span>

  <h1 class="headline">
    <span class="headline-lead">
      <span class="headline-number">5</span>
      <span class="headline-main">Tax Strategies</span>
    </span>
    <span class="headline-sub">Every Real Estate Agent<br>Should Know</span>
  </h1>

  <div class="brand-mark">
    <span class="brand-square"></span>
    <span class="brand-name">Birchwell</span>
  </div>

  <p class="presenter-line">Tax &amp; Legal Strategies for Real Estate Agents <span class="presented-by">Presented by</span> Birchwell Legal Partners, LLC</p>
  <p class="website">www.birchwelllegal.example</p>
</main>
</body>
</html>
```